LoanHarbor
I need double sided standard sized Business Card [3.5" x 2"]
Select font that compliments logo font
Simple
Pawel Merrin
Vice President - Purchase Division
4718 Birchwood Lane, Suite 300
Costa Mesa, CA 92681
Toll 800.517.2094
Direct 714.390.8152
Cell 949.306.7428
EFax 877.614.9087
pawelmerrin@loanharbor-example.net
www.loanharbor-example.net
NMLS# 748159
use periods in phone numbers instead of dashes. I like clean, aligned information and a lot of "negative" space. I want 2 versions one for the white background on white card, and one for the black background on a black card. Black card will be white on flip side.
This side is in the works. Will post very soon. Verbage.for both cards will be the same.

```html
<!DOCTYPE html>
<html lang="en">
<head>
<meta charset="utf-8">
<title>LoanHarbor Business Cards</title>
<link href="https://fonts.googleapis.com/css2?family=PT+Sans:wght@400;700&display=swap" rel="stylesheet">
<style>
  :root {
    --stage: #e9e6e2;
    --card-light: #ffffff;
    --card-dark-top: #2b2b2b;
    --card-dark-bottom: #151515;
    --brand-blue: #2a8fd0;
    --brand-blue-deep: #1668a8;
    --brand-blue-light: #6cc3f0;
    --ink: #3a3a3a;
    --ink-soft: #666666;
    --ink-on-dark: #e8e8e8;
    --silver: #b9bcc0;
    --divider-light: #c9c9c9;
    --divider-dark: #555555;
  }
  * { margin: 0; padding: 0; box-sizing: border-box; }
  html, body { width: 1200px; height: 852px; overflow: hidden; }
  body {
    background: var(--stage);
    font-family: "PT Sans", sans-serif;
    position: relative;
  }
  .card {
    position: absolute;
    width: 525px;
    height: 300px;
    border-radius: 16px;
    overflow: hidden;
    box-shadow: 0 6px 18px rgba(0,0,0,0.18);
  }
  .card--light { left: 110px; top: 110px; background: var(--card-light); color: var(--ink); }
  .card--dark {
    left: 565px; top: 442px;
    background: linear-gradient(160deg, var(--card-dark-top), var(--card-dark-bottom));
    color: var(--ink-on-dark);
  }
  .brand {
    position: absolute;
    left: 40px; top: 34px;
    display: flex; align-items: center; gap: 12px;
  }
  .brand-mark {
    width: 30px; height: 30px;
    background: var(--brand-blue);
  }
  .brand-name {
    font-size: 38px;
    font-weight: 400;
    color: var(--brand-blue-deep);
    letter-spacing: 0.2px;
  }
  .card--dark .brand-name { color: var(--ink-on-dark); }
  .holder {
    position: absolute;
    left: 40px; top: 108px;
    width: 180px;
    text-align: right;
    font-size: 12.5px;
    line-height: 1.38;
  }
  .holder-name {
    font-size: 17px;
    font-weight: 700;
    color: var(--brand-blue);
    margin-bottom: 1px;
  }
  .holder-title { font-weight: 700; margin-bottom: 3px; }
  .divider {
    position: absolute;
    left: 232px; top: 108px;
    width: 1px; height: 110px;
    background: var(--divider-light);
  }
  .card--dark .divider { background: var(--divider-dark); }
  .contacts {
    position: absolute;
    left: 244px; top: 106px;
    list-style: none;
    font-size: 12.5px;
    line-height: 18px;
  }
  .contacts li { display: flex; align-items: center; gap: 6px; }
  .contacts svg { width: 11px; height: 11px; flex: none; }
  .icon { fill: var(--brand-blue); }
  .swoosh { position: absolute; left: 0; bottom: 0; width: 525px; height: 80px; }
</style>
</head>
<body>

<svg width="0" height="0" style="position:absolute" aria-hidden="true">
  <defs>
    <symbol id="icon-phone" viewBox="0 0 12 12"><path d="M3 1l2 2-1 1.3c.6 1.4 1.5 2.3 2.7 2.8L8 6l2 2-1.5 2C5 9.6 2.4 7 2 3.5z"/></symbol>
    <symbol id="icon-cell" viewBox="0 0 12 12"><rect x="3" y="0.5" width="6" height="11" rx="1.2"/></symbol>
    <symbol id="icon-fax" viewBox="0 0 12 12"><rect x="1" y="4" width="10" height="6" rx="1"/><rect x="3" y="1" width="6" height="3"/></symbol>
    <symbol id="icon-mail" viewBox="0 0 12 12"><circle cx="6" cy="6" r="5.5"/></symbol>
    <symbol id="icon-web" viewBox="0 0 12 12"><path d="M6 .5a5.5 5.5 0 100 11 5.5 5.5 0 000-11zm0 1.5c.8 1 1.2 2.5 1.3 3.3H4.7C4.8 4.5 5.2 3 6 2zM4.7 6.7h2.6C7.2 7.5 6.8 9 6 10c-.8-1-1.2-2.5-1.3-3.3z"/></symbol>
    <linearGradient id="wave-blue" x1="0" x2="1" y1="0" y2="0">
      <stop offset="0" stop-color="#1668a8"/><stop offset="0.5" stop-color="#3fa7e3"/><stop offset="1" stop-color="#1a73b5"/>
    </linearGradient>
  </defs>
</svg>

<article class="card card--light">
  <div class="brand"><span class="brand-mark"></span><span class="brand-name">LoanHarbor</span></div>
  <div class="holder">
    <div class="holder-name">Pawel Merrin</div>
    <div class="holder-title">Vice President - Purchase Division</div>
    <div>4718 Birchwood Lane, Suite 300</div>
    <div>Costa Mesa, CA 92681</div>
    <div>Lic.no : NMLS# 748159</div>
  </div>
  <div class="divider"></div>
  <ul class="contacts">
    <li><svg class="icon"><use href="#icon-phone"/></svg>Toll 800.517.2094</li>
    <li><svg class="icon"><use href="#icon-phone"/></svg>Direct 714.390.8152</li>
    <li><svg class="icon"><use href="#icon-cell"/></svg>Cell 949.306.7428</li>
    <li><svg class="icon"><use href="#icon-fax"/></svg>EFax 877.614.9087</li>
    <li><svg class="icon"><use href="#icon-mail"/></svg>pawelmerrin@loanharbor-example.net</li>
    <li><svg class="icon"><use href="#icon-web"/></svg>www.loanharbor-example.net</li>
  </ul>
  <svg class="swoosh" viewBox="0 0 525 80" preserveAspectRatio="none">
    <path d="M0 44 C120 20 260 70 525 28 L525 80 L0 80Z" fill="url(#wave-blue)"/>
    <path d="M0 40 C120 16 260 66 525 24" fill="none" stroke="#b9bcc0" stroke-width="5"/>
    <path d="M0 62 C160 44 300 84 525 50 L525 80 L0 80Z" fill="#6cc3f0" opacity="0.55"/>
  </svg>
</article>

<article class="card card--dark">
  <div class="brand"><span class="brand-mark"></span><span class="brand-name">LoanHarbor</span></div>
  <div class="holder">
    <div class="holder-name">Pawel Merrin</div>
    <div class="holder-title">Vice President - Purchase Division</div>
    <div>4718 Birchwood Lane, Suite 300</div>
    <div>Costa Mesa, CA 92681</div>
    <div>Lic.no : NMLS# 748159</div>
  </div>
  <div class="divider"></div>
  <ul class="contacts">
    <li><svg class="icon"><use href="#icon-phone"/></svg>Toll 800.517.2094</li>
    <li><svg class="icon"><use href="#icon-phone"/></svg>Direct 714.390.8152</li>
    <li><svg class="icon"><use href="#icon-cell"/></svg>Cell 949.306.7428</li>
    <li><svg class="icon"><use href="#icon-fax"/></svg>EFax 877.614.9087</li>
    <li><svg class="icon"><use href="#icon-mail"/></svg>pawelmerrin@loanharbor-example.net</li>
    <li><svg class="icon"><use href="#icon-web"/></svg>www.loanharbor-example.net</li>
  </ul>
  <svg class="swoosh" viewBox="0 0 525 80" preserveAspectRatio="none">
    <path d="M0 44 C120 20 260 70 525 28 L525 80 L0 80Z" fill="url(#wave-blue)"/>
    <path d="M0 40 C120 16 260 66 525 24" fill="none" stroke="#b9bcc0" stroke-width="5"/>
    <path d="M0 62 C160 44 300 84 525 50 L525 80 L0 80Z" fill="#6cc3f0" opacity="0.45"/>
  </svg>
</article>

</body>
</html>
```